Harbor's Hymn Single Cover for iTunes etc

I am releasing a single out and I would like a simple cover design. This single cover will only be used online I.e. iTunes Spotify . I am going for a simple hipster rustic look. I have attached my photo that should be included in the design. If possible I would rather the photo just edited and words added . Thank you

Target Market(s)

Teens to 40s contempary Christians

Industry/Entity Type

Music Download

Requirements
Must have
• -The picture below
• -Marisol Penrow
• -Harbor's hymn

```html
<!DOCTYPE html>
<html lang="en">
<head>
<meta charset="utf-8">
<title>Harbor's Hymn — Marisol Penrow</title>
<link rel="stylesheet" href="https://fonts.googleapis.com/css2?family=Oswald:wght@300&family=Montserrat:wght@400&display=swap">
<style>
  :root {
    --parchment: #efe7d6;
    --parchment-light: #f7f1e4;
    --haze: #dccfb3;
    --frame-line: rgba(120, 96, 70, 0.35);
    --title-red: #8c2a12;
    --photo-light: #ead2a8;
    --photo-ember: #c2480f;
    --photo-deep: #6b1d0a;
    --photo-glow: #e58a2c;
    --photo-dark: #1e0a05;
    --name-cream: #f4e8cf;
  }
  * { margin: 0; padding: 0; box-sizing: border-box; }
  html, body {
    width: 1190px;
    height: 1200px;
    overflow: hidden;
    background: var(--parchment);
  }
  .cover {
    position: relative;
    width: 1190px;
    height: 1200px;
    overflow: hidden;
  }
  .cover__backdrop {
    position: absolute;
    inset: 0;
    background:
      radial-gradient(ellipse 55% 35% at 30% 60%, var(--haze) 0%, transparent 70%),
      linear-gradient(180deg, var(--parchment-light) 0%, var(--parchment) 55%, #e6dac2 100%);
  }
  .cover__photo {
    position: absolute;
    top: 0;
    right: 0;
    width: 800px;
    height: 1200px;
    background: linear-gradient(180deg,
      var(--photo-light) 0%,
      var(--photo-ember) 30%,
      var(--photo-deep) 52%,
      var(--photo-glow) 70%,
      var(--photo-deep) 84%,
      var(--photo-dark) 100%);
    -webkit-mask-image: linear-gradient(90deg, transparent 0%, #000 30%);
    mask-image: linear-gradient(90deg, transparent 0%, #000 30%);
  }
  .cover__frame {
    position: absolute;
    inset: 16px;
    border: 2px solid var(--frame-line);
    pointer-events: none;
  }
  .cover__title {
    position: absolute;
    left: 48px;
    top: 1145px;
    height: 125px;
    transform-origin: left top;
    transform: rotate(-90deg) scaleX(1.16);
    font-family: "Oswald", sans-serif;
    font-weight: 300;
    font-size: 125px;
    line-height: 125px;
    letter-spacing: 0.1em;
    text-transform: uppercase;
    color: var(--title-red);
    white-space: nowrap;
  }
  .cover__artist {
    position: absolute;
    left: 440px;
    top: 1098px;
    font-family: "Montserrat", sans-serif;
    font-weight: 400;
    font-size: 40px;
    line-height: 50px;
    letter-spacing: 0.55em;
    text-transform: uppercase;
    color: var(--name-cream);
    white-space: nowrap;
  }
</style>
</head>
<body>
  <main class="cover">
    <div class="cover__backdrop" role="img" aria-label="Faded rustic landscape of bare trees and a pale field in warm cream tones"></div>
    <div class="cover__photo" role="img" aria-label="Double-exposure photo of the singer blended with a glowing orange sunset"></div>
    <div class="cover__frame"></div>
    <h1 class="cover__title">Harbor's Hymn</h1>
    <p class="cover__artist">Marisol Penrow</p>
  </main>
</body>
</html>
```